I need Business Cards and Letterhead Designed

I have a current label so I just need the template design. It should be clean and should look rich. I own a Wealth Management/Investment Advisory business and I need to brand to look substantial & mature.

The Business Cards may be one or two sided and may be a standard or non-standard size. I will likely print on very thick stock but not a requirement. Embossment or foil are also something that I may consider but is not required.
Updates

Getting some great designs, thank you all for your hard work. I have returned from a trip and will be posting individual feedback over the next day or so. In the meantime please note the following:

1st. My disclosure should be posted at the bottom or back of the card. It may be in smaller print but it must be listed as follows "all together";

Securities offered through Veldmark Capital, Inc. A Registered Broker/Dealer. Member NAVRO/DLTB. Rick Halvern, Registered Representative. Advisory Services offered through Dunley Fairbrook an QVL Registered Investment Advisory Firm. ZRB Wealth Management, Veldmark Capital and Dunley Fairbrook are unaffiliated. CA Insurance Lic.# 7K42350

2nd. My Title should be listed as President / CEO
&
I need the following contact information included:

Address:
418 Perrin Way
Suite 2700
Costa Mesa, CA  90000

Phone; 555-318-0276
fax: 555-641-0093
email: rick.halvern@veldmarkcapitalmail.net

Thank you for your help.

Best regards,

RH

Target Market(s)

Affluent Individuals & Families. C-Level Executives, Women, Accountants, Attorneys, Business Owners

Industry/Entity Type

Business

Requirements
Must have
• Both my cards and letterhead must include the following disclosure:

Securities offered through Veldmark Capital, Inc. A Registered Broker/Dealer. Member NAVRO/DLTB.
Rick Halvern, Registered Representative. Advisory Services offered through Dunley Fairbrook an QVL Registered Investment Advisory Firm. ZRB Wealth Management, Veldmark Capital and Dunley Fairbrook are unaffiliated. CA Insurance Lic.# 7K4235
Should not have
• Do not include illustrations of money bags or gold bullion, or "$" signs or anything of that type.

```html
<!DOCTYPE html>
<html lang="en">
<head>
<meta charset="utf-8">
<title>ZRB Wealth Management – Business Card</title>
<link rel="stylesheet" href="https://fonts.googleapis.com/css2?family=Tinos:wght@400;700&display=swap">
<style>
  :root {
    --card-bg: #ffffff;
    --maroon: #4a2a2e;
    --texture-tan: #c9a67c;
    --texture-light: #d9bd96;
    --brand-brown: #5c2316;
    --accent-tan: #c3a488;
    --ink: #111111;
    --muted: #4a4a4a;
    --rule: #1a1a1a;
  }
  html, body {
    margin: 0;
    padding: 0;
    width: 1200px;
    height: 686px;
    overflow: hidden;
    background: var(--card-bg);
  }
  .card {
    position: relative;
    width: 1200px;
    height: 686px;
    background: var(--card-bg);
    font-family: "Tinos", "Times New Roman", serif;
    color: var(--ink);
  }
  .side-band {
    position: absolute;
    left: 0;
    top: 0;
    width: 159px;
    height: 686px;
    background: var(--maroon);
  }
  .side-texture {
    position: absolute;
    left: 0;
    top: 0;
    width: 159px;
    height: 194px;
    background: linear-gradient(160deg, var(--texture-light), var(--texture-tan));
  }
  .brand {
    position: absolute;
    left: 300px;
    top: 128px;
    display: flex;
    align-items: center;
    gap: 26px;
  }
  .brand-mark {
    width: 34px;
    height: 34px;
    background: var(--accent-tan);
  }
  .brand-name {
    margin: 0;
    font-size: 60px;
    font-weight: 400;
    line-height: 1;
    letter-spacing: 1px;
    color: var(--brand-brown);
  }
  .person {
    position: absolute;
    left: 360px;
    top: 218px;
    margin: 0;
    font-size: 24px;
    line-height: 1.3;
    color: var(--brand-brown);
    letter-spacing: 2px;
    text-transform: uppercase;
  }
  .contact-frame {
    position: absolute;
    left: 354px;
    top: 360px;
    width: 686px;
    height: 263px;
  }
  .contact-frame .rule-top {
    position: absolute;
    left: 0;
    top: 0;
    width: 686px;
    height: 2px;
    background: var(--rule);
  }
  .contact-frame .rule-side {
    position: absolute;
    left: 42px;
    top: 0;
    width: 2px;
    height: 263px;
    background: var(--rule);
  }
  .contact {
    position: absolute;
    right: 174px;
    top: 393px;
    margin: 0;
    font-style: normal;
    text-align: right;
    font-size: 29px;
    line-height: 1;
  }
  .contact .line { display: block; }
  .contact .street { margin-bottom: 23px; }
  .contact .city { margin-bottom: 37px; }
  .contact .phones { margin-bottom: 22px; }
  .contact .email { font-weight: 700; }
  .disclosure {
    position: absolute;
    left: 190px;
    right: 24px;
    top: 636px;
    margin: 0;
    font-size: 12px;
    line-height: 1.35;
    color: var(--muted);
    text-align: justify;
  }
</style>
</head>
<body>
  <main class="card">
    <div class="side-band"></div>
    <div class="side-texture" role="img" aria-label="Tan speckled paper texture panel"></div>

    <div class="brand">
      <span class="brand-mark"></span>
      <h1 class="brand-name">ZRB Wealth Management</h1>
    </div>

    <p class="person">Rick Halvern &nbsp;|&nbsp; President / CEO</p>

    <div class="contact-frame">
      <span class="rule-top"></span>
      <span class="rule-side"></span>
    </div>

    <address class="contact">
      <span class="line street">418 Perrin Way, Suite 2700</span>
      <span class="line city">Costa Mesa, CA&nbsp; 90000</span>
      <span class="line phones">555-318-0276&nbsp; 555-641-0093 fax</span>
      <span class="line email">rick.halvern@veldmarkcapitalmail.net</span>
    </address>

    <p class="disclosure">Securities offered through Veldmark Capital, Inc. A Registered Broker/Dealer. Member NAVRO/DLTB. Rick Halvern, Registered Representative. Advisory Services offered through Dunley Fairbrook an QVL Registered Investment Advisory Firm. ZRB Wealth Management, Veldmark Capital and Dunley Fairbrook are unaffiliated. CA Insurance Lic.# 7K42350</p>
  </main>
</body>
</html>
```